Wellness Flyer

I am seeking a flyer for my health and wellness company, Harbor Bloom. The flyer is to be DL size and single-sided. I am looking for a flyer that is both professional and fun looking, something similar to the uploaded files. Wording to include: (Please not wording to not include company name or logo but is rather advertising nutritional cleansing products)

Be your healthiest self. Take charge of your life. Get your best body.
Lose weight / Build muscle / Gain energy / Increase clarity
Start your journey to health and wellness. Transform your life
www.harborbloomco.com.au
Marisol@harborbloomco.com.au.
Natural . Raw. Organic . Cleansing system

Flyer needs to be single sided, DL size. I haven't uploaded my logo because I wanted to steer clear of having it on the flyer as it limits colour choice. Thanks.

Target Market(s)

Primarily Women 18-50.

Industry/Entity Type

Advertising

Font styles to use
Serif

Colors
34b8a4
fbed24

Requirements
Must have
• The wording as above.
Should not have
• Company name or Company logo

```html
<!DOCTYPE html>
<html lang="en">
<head>
<meta charset="utf-8">
<title>Be Your Healthiest Self – Wellness Flyer</title>
<link rel="stylesheet" href="https://fonts.googleapis.com/css2?family=Montserrat:wght@600;700;800&family=Lilita+One&display=swap">
<style>
  :root {
    --teal: #34b8a4;
    --teal-deep: #1a9c88;
    --teal-ink: #17917e;
    --teal-pale: #bfeae2;
    --mint: #e3f6f2;
    --sun: #f9b918;
    --lemon: #fbed24;
    --cream: #fff8e0;
    --white: #ffffff;
    --ink: #111111;
  }
  * { box-sizing: border-box; margin: 0; padding: 0; }
  html, body {
    width: 1200px; height: 2212px; overflow: hidden; background: var(--white);
  }
  .flyer {
    position: relative; width: 1200px; height: 2212px; overflow: hidden;
    font-family: "Montserrat", Arial, sans-serif;
  }
  .backdrop { position: absolute; inset: 0; width: 1200px; height: 2212px; }

  /* Header */
  .headline-rule {
    position: absolute; left: 150px; top: 52px; width: 5px; height: 180px; background: var(--white);
  }
  .headline {
    position: absolute; left: 170px; top: 52px;
    font-weight: 800; font-size: 58px; line-height: 1; color: var(--white); letter-spacing: 0.5px;
  }
  .headline-self {
    position: absolute; left: 166px; top: 112px;
    font-family: "Lilita One", Impact, sans-serif; font-size: 118px; line-height: 1;
    color: var(--sun); letter-spacing: 2px;
  }
  .headline-self-mirror {
    position: absolute; left: 430px; top: 112px;
    font-family: "Lilita One", Impact, sans-serif; font-size: 118px; line-height: 1;
    color: var(--teal-deep); opacity: 0.22; letter-spacing: 2px; transform: scaleX(-1);
  }

  /* Photo */
  .hero-photo {
    position: absolute; left: 0; top: 300px; width: 1200px; height: 640px;
    background:
      radial-gradient(ellipse at 30% 40%, #f3f7f4 0%, rgba(243,247,244,0) 55%),
      linear-gradient(180deg, #e7f0ec 0%, #d5e6e0 45%, #b9d98a 72%, #8fbf3c 100%);
  }
  .tagline {
    position: absolute; right: 80px; top: 355px;
    font-weight: 700; font-size: 40px; color: var(--ink); letter-spacing: -0.5px;
  }
  .promise {
    position: absolute; right: 78px; top: 420px; text-align: right;
    font-family: "Lilita One", Impact, sans-serif; font-size: 78px; line-height: 1.1;
    color: var(--lemon); -webkit-text-stroke: 3px var(--sun);
    text-shadow: 0 0 4px var(--white), 0 0 8px var(--white);
  }

  /* Benefits */
  .benefit {
    position: absolute; display: flex; align-items: center; gap: 34px;
    transform: translateX(-50%);
    font-family: "Lilita One", Impact, sans-serif; font-size: 68px; line-height: 1;
    color: var(--teal-deep); letter-spacing: 1px; white-space: nowrap;
    text-shadow: 0 3px 0 rgba(255,255,255,0.7);
  }
  .benefit svg { width: 62px; height: 48px; flex: none; }
  .benefit--weight  { left: 500px; top: 1220px; }
  .benefit--muscle  { left: 645px; top: 1356px; }
  .benefit--energy  { left: 512px; top: 1500px; }
  .benefit--clarity { left: 640px; top: 1636px; }

  .journey {
    position: absolute; left: 0; top: 1770px; width: 1200px; text-align: center;
    font-weight: 800; font-size: 32px; line-height: 1.32; color: var(--teal-ink);
  }

  /* Contact */
  .rsvp {
    position: absolute; left: 562px; top: 1897px; width: 124px; height: 38px;
    border-radius: 19px; background: var(--teal-pale);
    font-weight: 700; font-size: 22px; line-height: 38px; text-align: center; color: var(--teal-deep);
  }
  .contact {
    position: absolute; left: 0; top: 1938px; width: 1200px; text-align: center;
    font-weight: 600; font-size: 32px; line-height: 1.42; color: var(--white);
  }
  .range {
    position: absolute; left: 0; top: 2073px; width: 1200px; text-align: center;
    font-weight: 800; font-size: 38px; color: var(--teal-deep); letter-spacing: 0.5px;
  }
</style>
</head>
<body>
<main class="flyer">
  <svg class="backdrop" viewBox="0 0 1200 2212" aria-hidden="true">
    <defs>
      <radialGradient id="sunburst" cx="600" cy="1150" r="900" gradientUnits="userSpaceOnUse">
        <stop offset="0" stop-color="#fff6c2"/>
        <stop offset="0.25" stop-color="#fbd54a"/>
        <stop offset="0.6" stop-color="#f9b918"/>
        <stop offset="1" stop-color="#fbe28a"/>
      </radialGradient>
      <linearGradient id="stripe" x1="0" x2="1" y1="0" y2="0">
        <stop offset="0" stop-color="#ffffff" stop-opacity="0.95"/>
        <stop offset="0.5" stop-color="#ffffff" stop-opacity="0.55"/>
        <stop offset="1" stop-color="#ffffff" stop-opacity="0.95"/>
      </linearGradient>
      <radialGradient id="glow" cx="600" cy="1800" r="520" gradientUnits="userSpaceOnUse">
        <stop offset="0" stop-color="#ffffff" stop-opacity="0.95"/>
        <stop offset="1" stop-color="#ffffff" stop-opacity="0"/>
      </radialGradient>
    </defs>

    <!-- header band and waves -->
    <rect x="0" y="0" width="1200" height="320" fill="#ffffff"/>
    <path d="M0 0 H1200 V150 C900 230 400 110 0 200 Z" fill="var(--teal)"/>
    <path d="M0 200 C400 110 900 230 1200 150 V200 C900 270 380 170 0 250 Z" fill="var(--teal-pale)"/>
    <path d="M0 250 C380 170 900 270 1200 200 V320 H0 Z" fill="var(--mint)"/>
    <path d="M0 290 C350 250 800 330 1200 260" stroke="var(--teal)" stroke-width="10" fill="none" opacity="0.6"/>

    <!-- sun section -->
    <rect x="0" y="930" width="1200" height="980" fill="url(#sunburst)"/>
    <g fill="url(#stripe)">
      <rect x="0" y="1190" width="1200" height="34"/>
      <rect x="0" y="1262" width="1200" height="34"/>
      <rect x="0" y="1330" width="1200" height="30"/>
      <rect x="0" y="1400" width="1200" height="34"/>
      <rect x="0" y="1470" width="1200" height="30"/>
      <rect x="0" y="1544" width="1200" height="34"/>
      <rect x="0" y="1612" width="1200" height="30"/>
      <rect x="0" y="1686" width="1200" height="34"/>
    </g>
    <rect x="0" y="1600" width="1200" height="320" fill="url(#glow)"/>

    <!-- teal wave under photo -->
    <path d="M0 930 H1200 V960 C850 1030 400 1010 0 1060 Z" fill="var(--teal)"/>
    <path d="M0 1060 C400 1010 850 1030 1200 960 V1010 C850 1090 400 1070 0 1130 Z" fill="var(--teal-pale)" opacity="0.8"/>
    <path d="M120 1160 C400 1050 800 1040 1100 1150" stroke="#ffffff" stroke-width="14" fill="none" opacity="0.5"/>

    <!-- contact base -->
    <path d="M0 1930 C400 1880 800 1880 1200 1920 V2212 H0 Z" fill="var(--teal)"/>
    <ellipse cx="630" cy="1980" rx="360" ry="80" fill="#ffffff" opacity="0.12"/>
    <rect x="0" y="2045" width="1200" height="102" fill="var(--mint)"/>
    <rect x="0" y="2045" width="1200" height="6" fill="var(--teal-pale)"/>
    <rect x="0" y="2147" width="1200" height="65" fill="var(--teal)"/>
  </svg>

  <div class="hero-photo" role="img" aria-label="Photo of a woman stretching on sunlit grass in a park, city skyline behind"></div>

  <span class="headline-rule"></span>
  <h1 class="headline">BE YOUR HEALTHIEST</h1>
  <p class="headline-self">SELF</p>
  <p class="headline-self-mirror" aria-hidden="true">SELF</p>

  <p class="tagline">Take charge of your life.</p>
  <p class="promise">GET<br>YOUR BEST<br>BODY</p>

  <ul class="benefits">
    <li class="benefit benefit--weight"><svg viewBox="0 0 62 48"><polygon points="14,2 48,2 60,24 48,46 14,46 2,24" fill="var(--teal)"/><polygon points="14,2 48,2 60,24 2,24" fill="#ffffff" opacity="0.35"/></svg>LOSE WEIGHT<svg viewBox="0 0 62 48"><polygon points="14,2 48,2 60,24 48,46 14,46 2,24" fill="var(--teal)"/><polygon points="14,2 48,2 60,24 2,24" fill="#ffffff" opacity="0.35"/></svg></li>
    <li class="benefit benefit--muscle"><svg viewBox="0 0 62 48"><polygon points="14,2 48,2 60,24 48,46 14,46 2,24" fill="var(--teal)"/><polygon points="14,2 48,2 60,24 2,24" fill="#ffffff" opacity="0.35"/></svg>BUILD MUSCLE<svg viewBox="0 0 62 48"><polygon points="14,2 48,2 60,24 48,46 14,46 2,24" fill="var(--teal)"/><polygon points="14,2 48,2 60,24 2,24" fill="#ffffff" opacity="0.35"/></svg></li>
    <li class="benefit benefit--energy"><svg viewBox="0 0 62 48"><polygon points="14,2 48,2 60,24 48,46 14,46 2,24" fill="var(--teal)"/><polygon points="14,2 48,2 60,24 2,24" fill="#ffffff" opacity="0.35"/></svg>GAIN ENERGY<svg viewBox="0 0 62 48"><polygon points="14,2 48,2 60,24 48,46 14,46 2,24" fill="var(--teal)"/><polygon points="14,2 48,2 60,24 2,24" fill="#ffffff" opacity="0.35"/></svg></li>
    <li class="benefit benefit--clarity"><svg viewBox="0 0 62 48"><polygon points="14,2 48,2 60,24 48,46 14,46 2,24" fill="var(--teal)"/><polygon points="14,2 48,2 60,24 2,24" fill="#ffffff" opacity="0.35"/></svg>INCREASE CLARITY<svg viewBox="0 0 62 48"><polygon points="14,2 48,2 60,24 48,46 14,46 2,24" fill="var(--teal)"/><polygon points="14,2 48,2 60,24 2,24" fill="#ffffff" opacity="0.35"/></svg></li>
  </ul>

  <p class="journey">START YOUR JOURNEY TO HEALTH AND WELLNESS<br>TRANSFORM YOUR LIFE</p>

  <p class="rsvp">R.S.V.P</p>
  <p class="contact">www.harborbloomco.com.au<br>Marisol@harborbloomco.com.au.</p>

  <p class="range">NATURAL • RAW • ORGANIC • CLEANSING SYSTEM</p>
</main>
</body>
</html>
```